Harbor Vale needs a Business Card Design

We need a business card design for an Information Technology company based in Fairfax Virginia called Harbor Vale. We want the business card to use our logo colors. We need it to be double-sided. The business card needs to look professional but we would like it to be unique. You can get company information from our web site (http://www.harborvalellc.example).

Target Market(s)

Target market is Government Agencies and Business Professionals.

Industry/Entity Type

Business

Requirements
Must have
• Must have section for company name, company address, company URL, employee name, title, phone and email. Also must have company logo and space for entering logos.

```html
<!DOCTYPE html>
<html lang="en">
<head>
<meta charset="utf-8">
<title>Harbor Vale — Business Card</title>
<link rel="stylesheet" href="https://fonts.googleapis.com/css2?family=Montserrat:wght@400;500&family=Open+Sans:wght@400;600&family=Signika:wght@600&display=swap">
<style>
  :root {
    --stage: #d7d8da;
    --card: #ffffff;
    --navy: #27338f;
    --azure: #1877c0;
    --ink: #333a44;
    --muted: #6b7078;
    --rule: #8a8f96;
  }
  * { box-sizing: border-box; margin: 0; padding: 0; }
  html, body { width: 1200px; height: 900px; overflow: hidden; }
  body {
    background: var(--stage);
    font-family: "Open Sans", Arial, sans-serif;
    color: var(--ink);
    position: relative;
  }
  .card {
    position: absolute;
    width: 588px;
    height: 336px;
    border-radius: 22px;
    background: var(--card);
    box-shadow: 0 8px 24px rgba(0,0,0,.18);
    overflow: hidden;
  }
  .card--front { left: 110px; top: 70px; }
  .card--back { left: 502px; top: 494px; }

  .brand { display: flex; align-items: center; gap: 14px; }
  .brand__square { width: 44px; height: 44px; background: var(--navy); }
  .brand__name {
    font-family: "Signika", "Open Sans", sans-serif;
    font-weight: 600;
    font-size: 30px;
    color: var(--navy);
    letter-spacing: .5px;
  }
  .card--front .brand { position: absolute; left: 36px; top: 38px; }

  .person { position: absolute; left: 64px; top: 130px; width: 300px; }
  .person__name {
    font-family: "Montserrat", sans-serif;
    font-weight: 500;
    font-size: 22px;
    letter-spacing: 1.5px;
    text-transform: uppercase;
    color: #2b2f36;
  }
  .person__title {
    font-size: 11px;
    font-weight: 600;
    font-variant: small-caps;
    letter-spacing: 1px;
    color: var(--muted);
    margin-top: 1px;
  }
  .dotted { border-top: 1.5px dotted var(--rule); margin: 6px 0 8px; }
  .contact { list-style: none; }
  .contact li {
    display: flex; align-items: center; gap: 14px;
    font-size: 14px; color: var(--muted); line-height: 22px;
  }
  .contact svg { width: 16px; height: 16px; flex: none; }
  .address { font-size: 15px; color: var(--muted); line-height: 24px; margin-top: 4px; }

  .card--back { background: var(--azure); }
  .back__band {
    position: absolute; left: 0; top: 0; width: 100%; height: 120px;
    background: var(--navy);
  }
  .card--back .brand { position: absolute; left: 40px; top: 150px; }
  .card--back .brand__square { background: #ffffff; }
  .card--back .brand__name { color: #ffffff; font-size: 46px; }
</style>
</head>
<body>
  <section class="card card--front" aria-label="Business card front">
    <div class="brand">
      <span class="brand__square"></span>
      <span class="brand__name">Harbor Vale</span>
    </div>
    <div class="person">
      <h1 class="person__name">Daniel Reyes</h1>
      <p class="person__title">Executive Creative Director</p>
      <div class="dotted"></div>
      <ul class="contact">
        <li>
          <svg viewBox="0 0 16 16" aria-hidden="true"><path d="M4 2l2.5 3-1.4 1.6a8 8 0 0 0 4.3 4.3L11 9.5 14 12l-1.5 2C7 14 2 9 2 3.5z" fill="var(--muted)"/></svg>
          : + 1 703-555-0148
        </li>
        <li>
          <svg viewBox="0 0 16 16" aria-hidden="true"><rect x="1.5" y="3.5" width="13" height="9" fill="none" stroke="var(--muted)"/><path d="M1.5 3.5l6.5 5 6.5-5" fill="none" stroke="var(--muted)"/></svg>
          : daniel.r@harborvalellc.example
        </li>
        <li>
          <svg viewBox="0 0 16 16" aria-hidden="true"><circle cx="8" cy="8" r="6.5" fill="none" stroke="var(--muted)"/><ellipse cx="8" cy="8" rx="3" ry="6.5" fill="none" stroke="var(--muted)"/><path d="M1.5 8h13M2.5 5h11M2.5 11h11" stroke="var(--muted)" stroke-width=".8"/></svg>
          : www.harborvalellc.example
        </li>
      </ul>
      <div class="dotted"></div>
      <p class="address">4100 Chain Bridge Rd, Suite 200<br>Fairfax, Virginia, United States</p>
    </div>
  </section>

  <section class="card card--back" aria-label="Business card back">
    <div class="back__band"></div>
    <div class="brand">
      <span class="brand__square"></span>
      <span class="brand__name">Harbor Vale</span>
    </div>
  </section>
</body>
</html>
```